Corvane Industries business cards

We need business cards for our company Corvane Industries, based in Brisbane but trading world wide. We buy and sell Corvane Industries, generators and marine equipment. The design needs to be kept clean, simple but eye catching.
Please keep with our current logo (included) and further information can be included on request

Business

0792cd
33a6d7
85cae6
3276b5
0455a3
cedeed
cee9f5
ffffff

```html
<!DOCTYPE html>
<html lang="en">
<head>
<meta charset="utf-8">
<title>Corvane Industries – Business Cards</title>
<link href="https://fonts.googleapis.com/css2?family=Roboto:wght@400&family=Open+Sans:wght@400;600;700&display=swap" rel="stylesheet">
<style>
  :root {
    --backdrop: #e4e6e9;
    --card: #ffffff;
    --brand: #3f87c4;
    --brand-dark: #2f78bb;
    --text: #5f6063;
    --rule: #9a9ca0;
  }
  * { margin: 0; padding: 0; box-sizing: border-box; }
  html, body { width: 1200px; height: 1000px; overflow: hidden; }
  body { background: var(--backdrop); font-family: "Open Sans", Arial, sans-serif; position: relative; }

  .card {
    position: absolute; left: 265px; width: 665px; height: 397px;
    background: var(--card); border-radius: 24px;
    box-shadow: 0 4px 14px rgba(0,0,0,0.18);
  }
  .card--front { top: 73px; }
  .card--back { top: 533px; }

  .brand { position: absolute; display: flex; align-items: flex-start; }
  .brand__mark { background: var(--brand); border-radius: 8px; flex: none; }
  .brand__name {
    font-family: "Roboto", Arial, sans-serif; font-weight: 400; color: var(--brand);
    display: flex; flex-direction: column;
  }
  .brand__suffix { align-self: flex-end; }

  .card--front .brand { left: 40px; top: 45px; }
  .card--front .brand__mark { width: 83px; height: 83px; margin-right: 13px; }
  .card--front .brand__name { font-size: 44px; line-height: 46px; }
  .card--front .brand__suffix { font-size: 15px; line-height: 16px; }

  .holder {
    position: absolute; left: 40px; top: 200px;
    font-weight: 700; font-size: 20px; color: var(--brand-dark);
    padding-bottom: 3px; border-bottom: 3px solid var(--brand-dark);
  }
  .holder-rule { position: absolute; left: 198px; right: 38px; top: 228px; height: 1px; background: var(--rule); }

  .contacts { position: absolute; left: 40px; top: 251px; list-style: none; }
  .contacts li { display: flex; align-items: center; font-size: 15px; line-height: 20.5px; color: var(--text); }
  .contacts svg { width: 11px; height: 11px; margin-right: 8px; fill: var(--brand-dark); flex: none; }
  .contacts strong { color: var(--brand-dark); font-weight: 400; }

  .addresses { position: absolute; right: 39px; top: 239px; text-align: right; font-size: 15px; line-height: 19px; color: var(--text); }
  .addresses h3 { font-size: 15px; font-weight: 600; color: var(--brand-dark); }
  .addresses p + h3 { margin-top: 4px; }

  .card--back .brand { left: 115px; top: 119px; }
  .card--back .brand__mark { width: 122px; height: 122px; margin-right: 22px; }
  .card--back .brand__name { font-size: 66px; line-height: 66px; margin-top: -6px; }
  .card--back .brand__suffix { font-size: 22px; line-height: 24px; }

  .web { position: absolute; left: 0; right: 0; top: 332px; text-align: center; font-size: 15px; color: var(--brand-dark); }
  .web strong { font-weight: 600; }
</style>
</head>
<body>

<section class="card card--front">
  <div class="brand">
    <div class="brand__mark"></div>
    <div class="brand__name"><span>Corvane</span><span>Industries</span><span class="brand__suffix">Pty Ltd</span></div>
  </div>

  <h2 class="holder">Marla Quenby</h2>
  <div class="holder-rule"></div>

  <ul class="contacts">
    <li><svg viewBox="0 0 12 12"><path d="M3 0h6v12H3z M4 1v9h4V1z" fill-rule="evenodd"/></svg>+61 400 555 218</li>
    <li><svg viewBox="0 0 12 12"><path d="M0 3q6-4 12 0v2H9V4H3v1H0z M2 6h8l1 5H1z"/></svg>+61 7 3000 4820</li>
    <li><svg viewBox="0 0 12 12"><path d="M3 0h6v3H3z M0 4h12v5H10v3H2V9H0z M3 8v3h6V8z" fill-rule="evenodd"/></svg>+61 7 3000 4821</li>
    <li><svg viewBox="0 0 12 12"><path d="M0 2h12v8H0z M1 3l5 4 5-4z" fill-rule="evenodd"/></svg>marla@corvane-ind.com.au</li>
    <li><svg viewBox="0 0 12 12"><circle cx="6" cy="6" r="5.5" fill="none" stroke="#2f78bb"/><path d="M0.5 6h11M6 0.5v11" stroke="#2f78bb" fill="none"/><ellipse cx="6" cy="6" rx="2.5" ry="5.5" fill="none" stroke="#2f78bb"/></svg>www.<strong>corvane-ind</strong>.com.au</li>
  </ul>

  <div class="addresses">
    <h3>Adress Location</h3>
    <p>18 Tallow Street<br>HARMONT QLD 4175</p>
    <h3>Postal Address</h3>
    <p>PO Box 902,<br>Kelvale QLD 4178</p>
  </div>
</section>

<section class="card card--back">
  <div class="brand">
    <div class="brand__mark"></div>
    <div class="brand__name"><span>Corvane</span><span>Industries</span><span class="brand__suffix">Pty Ltd</span></div>
  </div>
  <p class="web">www.<strong>corvane-ind</strong>.com.au</p>
</section>

</body>
</html>
```